1. Overview of company:
Copper Fern Mobile solutions private Ltd is one of the leading innovators & providers of Value added services (VAS) and telecom solutions to the top telecom operators across the world. We are the pioneer of several telecom technologies and products with our solutions empowering over 40 telecom giant in 51 countries.

2. Product Overview:
Vocal Twist is the most innovative voice morphing mobile app that has revolutionized the concept of IVR based offerings for telecom operators across the world. It lets you talk to your friend in a voice of your choice at just the press of a button. In addition to every call, users can now speak to their friends with background sounds of their choice.

In simple words: If person A calls person B, person A can choose the voice he wants B to listen, Words and sentences remain same just the voice changes. Person A can even activate a background sound for both of them while talking.

3. Objective of the design:
The purpose of this campaign is to establish Vocal Twist as Innovative, Lively, Youthful, Fun mobile app generally used for spreading smiles via pranks. The primary objective is to persuade the audience to download and use Vocal Twist mobile app, as well as to spread and characterize this new app.

4. Product layout:
Page 1: Landing Page
- pictorial explanation, what Vocal Twist stands for

Page 2: Home Screen options
-Navigation to vocal twist
-Navigation to sound scenery

Page 3: Vocal Twist options
-Female
-Cartoon
-King
-Bunny

Page 4: Sound scenery options
-Romantic
-Airport
-Traffic
-Football
-Church
-Beach

5. Target Audience
The users of the mobile app will be teenager whose age ranges from 16-27. The demographics are not restricted to a particular country and will be present on global level.

6. Deliverable
- 4 Uncoded screen and icon for mobile app "Vocal Twist"
- Our company name is "Copper Fern" , we would like to see designs that use Black and Green, at the same time its not mandatory.
-Design should communicate what the app stands for "Changing voice of caller"

Target Market(s)

User of the mobile app will be teenagers whose age ranges from 16-27. The demographics are not restricted to a particular country and will be present on global level. It's for masses.

Industry/Entity Type

Telecommunications

Requirements
Must have
• The design should be self explanatory, what the app stands for.
• Editable format for integration purpose.
Nice to have
• Would prefer Icons and very few words.
• Professional, elegant at the same time trendy designs.

```html
<!DOCTYPE html>
<html lang="en">
<head>
<meta charset="utf-8">
<title>Vocal Twist – Sound Scenery</title>
<link rel="stylesheet" href="https://fonts.googleapis.com/css2?family=Lato:wght@300;400;700&display=swap">
<style>
  :root {
    --black: #161616;
    --header: #141414;
    --green: #4caf50;
    --green-soft: #5dba61;
    --white: #ffffff;
    --grey-select: #666666;
    --status-grey: #8a8a8a;
  }
  * { box-sizing: border-box; margin: 0; padding: 0; }
  html, body { width: 675px; height: 1200px; overflow: hidden; background: var(--black); }
  body { font-family: "Lato", sans-serif; color: var(--white); }

  .screen { position: relative; width: 675px; height: 1200px; overflow: hidden;
    background: radial-gradient(circle at 50% 78%, #262626 0%, var(--black) 60%); }

  .status-bar { position: absolute; top: 0; left: 0; width: 100%; height: 40px; background: var(--header);
    font-size: 20px; display: flex; align-items: center; justify-content: space-between; padding: 0 12px; }
  .status-left { display: flex; align-items: center; gap: 6px; }
  .signal { display: flex; gap: 3px; }
  .signal span { width: 9px; height: 9px; border-radius: 50%; background: var(--white); }
  .status-time { position: absolute; left: 0; right: 0; text-align: center; font-weight: 700; pointer-events: none; }
  .status-right { display: flex; align-items: center; gap: 8px; }
  .battery { width: 40px; height: 18px; border: 2px solid var(--white); border-radius: 3px; position: relative; padding: 2px; }
  .battery::after { content: ""; position: absolute; right: -5px; top: 4px; width: 3px; height: 6px; background: var(--white); border-radius: 0 2px 2px 0; }
  .battery-level { width: 22%; height: 100%; background: var(--white); }

  .app-header { position: absolute; top: 40px; left: 0; width: 100%; height: 75px; background: var(--header);
    display: flex; align-items: center; justify-content: center; }
  .app-title { font-size: 31px; font-weight: 700; letter-spacing: 0.5px; }

  .hero { position: absolute; top: 115px; left: 0; width: 100%; height: 405px; background: var(--green); text-align: center; }
  .hero-emblem { position: absolute; left: 227px; top: 83px; width: 223px; height: 140px;
    background: radial-gradient(ellipse at center, var(--green-soft) 0%, var(--green) 75%); border-radius: 12px; }
  .hero-title { position: absolute; top: 248px; width: 100%; font-size: 43px; font-weight: 300; letter-spacing: 1.5px; }
  .hero-subtitle { position: absolute; top: 308px; width: 100%; font-size: 25px; font-weight: 300; letter-spacing: 1.6px; }

  .effect { position: absolute; width: 250px; height: 250px; text-align: center; }
  .effect-icon { position: absolute; left: 50%; transform: translateX(-50%); }
  .effect-label { position: absolute; width: 100%; left: 0; font-size: 32px; font-weight: 400; }

  .effect--selected .effect-ring { position: absolute; left: 13px; top: 13px; width: 224px; height: 224px; border-radius: 50%; background: var(--grey-select); }
  .effect-check { position: absolute; left: 102px; top: 212px; width: 46px; height: 46px; border-radius: 50%; background: var(--green);
    display: flex; align-items: center; justify-content: center; }

  .effect--romantic { left: 48px; top: 557px; }
  .effect--airport { left: 382px; top: 557px; }
  .effect--traffic { left: 46px; top: 874px; }
  .effect--football { left: 384px; top: 874px; }
</style>
</head>
<body>
<main class="screen">
  <div class="status-bar">
    <div class="status-left">
      <div class="signal"><span></span><span></span><span></span><span></span><span></span></div>
      <span class="carrier">ORBIT</span>
      <svg width="20" height="15" viewBox="0 0 20 15" aria-hidden="true">
        <path d="M10 14 L6.5 10.2 A5 5 0 0 1 13.5 10.2 Z" fill="#fff"/>
        <path d="M3.7 7.4 A9 9 0 0 1 16.3 7.4" stroke="#fff" stroke-width="2" fill="none"/>
        <path d="M1 4.4 A13 13 0 0 1 19 4.4" stroke="#fff" stroke-width="2" fill="none"/>
      </svg>
    </div>
    <div class="status-time">4:21 PM</div>
    <div class="status-right">
      <svg width="12" height="20" viewBox="0 0 12 20" aria-hidden="true">
        <path d="M1 5 L10 14 L5.5 18.5 V1.5 L10 6 L1 15" stroke="var(--status-grey)" stroke-width="1.6" fill="none"/>
      </svg>
      <span>22%</span>
      <div class="battery"><div class="battery-level"></div></div>
    </div>
  </div>

  <header class="app-header"><h1 class="app-title">VOCAL TWIST</h1></header>

  <section class="hero">
    <div class="hero-emblem" role="img" aria-label="Sound Scenery emblem: flowing wave lines with three stars"></div>
    <h2 class="hero-title">Sound Scenery</h2>
    <p class="hero-subtitle">Choose from the effects below</p>
  </section>

  <div class="effect effect--romantic effect--selected">
    <div class="effect-ring"></div>
    <svg class="effect-icon" style="top:52px" width="110" height="100" viewBox="0 0 110 100" aria-hidden="true">
      <path d="M55 98 C40 82 4 58 4 30 C4 12 18 2 32 2 C44 2 51 9 55 16 C59 9 66 2 78 2 C92 2 106 12 106 30 C106 58 70 82 55 98 Z" fill="#fff"/>
      <path d="M88 10 C98 14 103 22 101 34 C98 24 94 17 84 14 Z" fill="var(--grey-select)"/>
    </svg>
    <div class="effect-label" style="top:170px">Romantic</div>
    <div class="effect-check">
      <svg width="26" height="20" viewBox="0 0 26 20" aria-hidden="true"><path d="M3 10 L10 17 L23 3" stroke="#fff" stroke-width="4" fill="none" stroke-linecap="round" stroke-linejoin="round"/></svg>
    </div>
  </div>

  <div class="effect effect--airport">
    <svg class="effect-icon" style="top:50px" width="122" height="90" viewBox="0 0 122 90" aria-hidden="true">
      <path d="M4 30 L12 28 L26 42 L52 32 L38 8 L48 6 L76 26 L104 14 C114 10 122 10 120 16 C118 22 108 26 100 30 L30 58 C22 61 14 58 10 52 Z" fill="#fff"/>
      <rect x="2" y="80" width="120" height="9" rx="4.5" fill="#fff"/>
    </svg>
    <div class="effect-label" style="top:170px">Airport</div>
  </div>

  <div class="effect effect--traffic">
    <svg class="effect-icon" style="top:75px" width="102" height="102" viewBox="0 0 102 102" aria-hidden="true">
      <path d="M22 0 H80 A4 4 0 0 1 84 4 V16 H102 C100 26 94 30 84 32 V40 H102 C100 50 94 54 84 56 V64 H102 C100 74 94 78 84 80 V98 A4 4 0 0 1 80 102 H22 A4 4 0 0 1 18 98 V80 C8 78 2 74 0 64 H18 V56 C8 54 2 50 0 40 H18 V32 C8 30 2 26 0 16 H18 V4 A4 4 0 0 1 22 0 Z" fill="#fff"/>
      <circle cx="51" cy="21" r="12" fill="var(--black)"/>
      <circle cx="51" cy="51" r="12" fill="var(--black)"/>
      <circle cx="51" cy="81" r="12" fill="var(--black)"/>
    </svg>
    <div class="effect-label" style="top:210px">Traffic</div>
  </div>

  <div class="effect effect--football">
    <svg class="effect-icon" style="top:72px" width="116" height="116" viewBox="0 0 116 116" aria-hidden="true">
      <circle cx="58" cy="58" r="55" fill="#fff"/>
      <circle cx="58" cy="58" r="51" fill="none" stroke="var(--black)" stroke-width="3"/>
      <polygon points="58,46 72,56 67,73 49,73 44,56" fill="var(--black)"/>
      <g stroke="var(--black)" stroke-width="3" fill="none">
        <path d="M58 46 V22 M72 56 L94 48 M67 73 L80 94 M49 73 L36 94 M44 56 L22 48"/>
        <path d="M58 22 L40 14 M58 22 L76 14 M94 48 L104 34 M94 48 L104 68 M80 94 L98 86 M80 94 L70 108 M36 94 L46 108 M36 94 L18 86 M22 48 L12 34 M22 48 L12 68"/>
      </g>
      <polygon points="46,8 58,4 70,8 58,14" fill="var(--black)"/>
      <polygon points="106,44 110,58 106,72 100,58" fill="var(--black)"/>
      <polygon points="10,44 16,58 10,72 6,58" fill="var(--black)"/>
      <polygon points="90,98 80,106 72,108 78,98" fill="var(--black)"/>
      <polygon points="26,98 36,106 44,108 38,98" fill="var(--black)"/>
    </svg>
    <div class="effect-label" style="top:210px">Football</div>
  </div>
</main>
</body>
</html>
```